Coffeeshop menu for filter tip

We want to have a cannabis (coffeeshop) menu in the size 25mm wide x 60mm wide. Some examples attached.

it must have the following text:
Menu

WEED p/g
Velotrine €16
Cinderfox €14
Tide Rambler €14
Marigolden €16
Grand Pelican €14
Copper Comet €14

HASH p/g
Baltic Ember €12
Harbor Velvet€11
Plum Rova €14
Dusk Maple €10

Target Market(s)

tourist in Amsterdam

Requirements
Nice to have
• cannabis sign leaf
• No Cigarettes allowed symbol

```html
<!DOCTYPE html>
<html lang="en">
<head>
<meta charset="utf-8">
<title>Coffeeshop Menu</title>
<link rel="stylesheet" href="https://fonts.googleapis.com/css2?family=Patrick+Hand&display=swap">
<style>
  :root {
    --bg: #3b4f3c;
    --leaf: #109d4b;
    --text: #f2e20f;
    --sign-ring: #b9503c;
    --sign-fill: #a4ad9f;
    --sign-mark: #2f2f2f;
  }
  html, body {
    margin: 0;
    padding: 0;
    width: 1200px;
    height: 2880px;
    overflow: hidden;
    background: var(--bg);
  }
  .menu-card {
    position: relative;
    width: 1200px;
    height: 2880px;
    background: var(--bg);
    color: var(--text);
    overflow: hidden;
    font-family: "Patrick Hand", cursive;
  }
  .backdrop {
    position: absolute;
    inset: 0;
    background: linear-gradient(to bottom, var(--bg) 0%, var(--bg) 30%, var(--leaf) 78%, var(--leaf) 100%);
  }
  .menu-title,
  .section-title {
    position: absolute;
    left: 78px;
    margin: 0;
    font-weight: 400;
    line-height: 1;
  }
  .menu-title { top: 97px; font-size: 380px; }
  .section-title { font-size: 220px; }
  .section-title.weed { top: 532px; }
  .section-title.hash { top: 1760px; }
  .unit {
    position: absolute;
    right: 80px;
    font-size: 104px;
    line-height: 1;
  }
  .unit.weed { top: 660px; }
  .unit.hash { top: 1880px; }
  .price-list {
    position: absolute;
    left: 81px;
    right: 80px;
    margin: 0;
    padding: 0;
    list-style: none;
    font-size: 100px;
    line-height: 91px;
  }
  .price-list.weed { top: 830px; }
  .price-list.hash { top: 2038px; }
  .price-item {
    display: flex;
    align-items: baseline;
    height: 91px;
  }
  .item-name, .item-price { white-space: nowrap; }
  .leader {
    flex: 1;
    margin: 0 4px;
    border-bottom: 6px dotted var(--text);
    transform: translateY(-6px);
  }
  .no-smoking {
    position: absolute;
    left: 950px;
    top: 2630px;
    width: 212px;
    height: 212px;
  }
</style>
</head>
<body>
<main class="menu-card">
  <div class="backdrop" role="img" aria-label="Large green cannabis leaf illustration behind the menu"></div>

  <h1 class="menu-title">Menu</h1>

  <h2 class="section-title weed">Weed</h2>
  <span class="unit weed">p/g</span>
  <ul class="price-list weed">
    <li class="price-item"><span class="item-name">Velotrine</span><span class="leader"></span><span class="item-price">€16</span></li>
    <li class="price-item"><span class="item-name">Cinderfox</span><span class="leader"></span><span class="item-price">€14</span></li>
    <li class="price-item"><span class="item-name">Tide Rambler</span><span class="leader"></span><span class="item-price">€14</span></li>
    <li class="price-item"><span class="item-name">Marigolden</span><span class="leader"></span><span class="item-price">€16</span></li>
    <li class="price-item"><span class="item-name">Grand Pelican</span><span class="leader"></span><span class="item-price">€14</span></li>
    <li class="price-item"><span class="item-name">Copper Comet</span><span class="leader"></span><span class="item-price">€14</span></li>
  </ul>

  <h2 class="section-title hash">Hash</h2>
  <span class="unit hash">p/g</span>
  <ul class="price-list hash">
    <li class="price-item"><span class="item-name">Baltic Ember</span><span class="leader"></span><span class="item-price">€12</span></li>
    <li class="price-item"><span class="item-name">Harbor Velvet</span><span class="leader"></span><span class="item-price">€11</span></li>
    <li class="price-item"><span class="item-name">Plum Rova</span><span class="leader"></span><span class="item-price">€14</span></li>
    <li class="price-item"><span class="item-name">Dusk Maple</span><span class="leader"></span><span class="item-price">€10</span></li>
  </ul>

  <svg class="no-smoking" viewBox="0 0 220 220" role="img" aria-label="No smoking sign">
    <circle cx="110" cy="110" r="96" fill="var(--sign-fill)" stroke="var(--sign-ring)" stroke-width="20"/>
    <rect x="38" y="112" width="118" height="22" fill="var(--sign-mark)"/>
    <rect x="160" y="112" width="8" height="22" fill="var(--sign-mark)"/>
    <rect x="172" y="112" width="8" height="22" fill="var(--sign-mark)"/>
    <path d="M150 100 C140 80 170 72 160 52 M166 100 C158 84 186 76 176 58" fill="none" stroke="var(--sign-mark)" stroke-width="5" stroke-linecap="round"/>
    <line x1="42" y1="42" x2="178" y2="178" stroke="var(--sign-ring)" stroke-width="20"/>
  </svg>
</main>
</body>
</html>
```